The Amp Fellow

need a business card for a dj and sound equipment hire(rentals) business based in Melbourne. i have attached a current card get an idea. card needs to be unique professional looking.

ps.this card is not for a DJ. it's a rental business of dj equipment and pa systems.

Industry/Entity Type

Business

Font styles to use
Sans Serif
Script

Requirements
Must have
• Business Name: THE AMP FELLOW
Contact Person: RAVINDU PERERALA
Mobile: 047 BASSY 82
Email: RAVINDU@THEAMPFELLOW.COM.AU
Website: WWW.THEAMPFELLOW.COM.AU
Facebook: WWW.FACEBOOK.CM/THEAMPFELLOW.COM.AU

```html
<!DOCTYPE html>
<html lang="en">
<head>
<meta charset="utf-8">
<title>The Amp Fellow – Business Card</title>
<link rel="stylesheet" href="https://fonts.googleapis.com/css2?family=Arimo:wght@400;700&family=Dancing+Script:wght@400&display=swap">
<style>
  :root {
    --page: #ffffff;
    --card: #ffffff;
    --ink: #555658;
    --blue: #0ea0dc;
    --blue-mid: #2cb6ea;
    --blue-soft: #93d4f1;
    --mark: #3a3b3d;
  }
  * { margin: 0; padding: 0; box-sizing: border-box; }
  html, body {
    width: 1200px;
    height: 848px;
    overflow: hidden;
    background: var(--page);
    font-family: "Arimo", Arial, sans-serif;
  }
  .business-card {
    position: absolute;
    left: 322px;
    top: 265px;
    width: 556px;
    height: 335px;
    background: var(--card);
    border-radius: 10px;
    overflow: hidden;
    box-shadow: 0 0 0 1px rgba(0,0,0,0.04);
  }
  .sound-band {
    position: absolute;
    left: 16px;
    top: 0;
    width: 530px;
    height: 148px;
    background: linear-gradient(to bottom,
      var(--blue) 0%,
      var(--blue) 45%,
      var(--blue-mid) 65%,
      var(--blue-soft) 85%,
      rgba(147,212,241,0) 100%);
  }

  .brand {
    position: absolute;
    left: 20px;
    top: 218px;
    width: 100px;
    display: flex;
    flex-direction: column;
    align-items: center;
    gap: 14px;
  }
  .brand-dot {
    width: 58px;
    height: 58px;
    border-radius: 50%;
    background: var(--mark);
  }
  .brand-name {
    font-family: "Dancing Script", cursive;
    font-size: 17px;
    font-weight: 400;
    color: var(--mark);
    white-space: nowrap;
  }

  .contact {
    position: absolute;
    right: 20px;
    bottom: 15px;
    text-align: right;
  }
  .contact-name {
    font-size: 20px;
    font-weight: 700;
    color: var(--ink);
    letter-spacing: 0.3px;
    line-height: 24px;
    margin-bottom: 4px;
  }
  .contact-line {
    font-size: 11px;
    line-height: 14px;
    color: var(--blue);
  }
  .contact-line .plus,
  .contact-line .word { color: var(--ink); }
  .contact-line.plus-line .plus { font-size: 14px; font-weight: 700; }
  .contact-line.website { font-weight: 700; }
</style>
</head>
<body>
  <main class="business-card">
    <div class="sound-band" role="img" aria-label="Blue equalizer-style sound level pattern"></div>

    <div class="brand">
      <span class="brand-dot"></span>
      <span class="brand-name">The Amp Fellow</span>
    </div>

    <section class="contact">
      <h1 class="contact-name">RAVINDU PERERALA</h1>
      <p class="contact-line plus-line"><span class="plus">+</span> 047 <span class="word">BASSY</span> 82</p>
      <p class="contact-line">ravindu@theampfellow.com.au</p>
      <p class="contact-line">www.facebook.cm/theampfellow.com.au</p>
      <p class="contact-line website">www.theampfellow.com.au</p>
    </section>
  </main>
</body>
</html>
```